Masculine Van wrap design for a cleaning company

I would like a design for my property maintenance van. I would like an eye catching and more so masculine design.
Very simple yet modern - think classic plumbing company design but modern
We work in Jersey City across from NYC in condominiums and apartment buildings.
The van is a 2013 Kestro cargo 2500
The color is white - I think gold(burnt yellow) and black will contrast nicely
Went on vacation/holiday
Target Market(s)
apartment building owners
Industry/Entity Type
Cleaning Service
Requirements
Must have
- Drivers side of van (entire length): Logo, Under Logo: Shared Lobby Residence Upkeep
- under Shared Lobby Residence Upkeep: www.BirchKSN.com, under website: (555) 314 - 7260
- Passenger side (same as right): Logo, Under Logo: Shared Lobby Residence Upkeep under S.L.R.U,: www.BirchKSN.com, under website: (555) 314 - 7260
- Servicing Hoboken & Jersey City ( on side anywhere that may fit)
- Back: Right Side door: Logo, under logo: website. Left side door: Shared Lobby Residence Upkeep, under S.L.R.U: 555 314 7260. Under cell phone, Servicing Jersey City & Hoboken
Nice to have
- Colors: black, burnt yellow or burgundy
Should not have
- too much clutter or images. More professional than fun

```html
<!DOCTYPE html>
<html lang="en">
<head>
<meta charset="utf-8">
<title>Birch Keystone Property Maintenance – Van Wrap</title>
<link rel="stylesheet" href="https://fonts.googleapis.com/css2?family=Cinzel:wght@400;600&family=Marcellus&display=swap">
<style>
  :root {
    --page: #eceae6;
    --wrap-white: #ffffff;
    --gold: #c98f2b;
    --gold-deep: #8a6418;
    --olive: #3f3213;
    --burgundy: #6a1431;
    --black: #121212;
    --glass: #3a3f43;
    --tyre: #1b1b1b;
    --rim: #c9cccf;
    --tail: #b3122a;
    --text-light: #f4efe4;
  }
  html, body {
    margin: 0;
    width: 1200px;
    height: 800px;
    overflow: hidden;
    background: var(--page);
  }
  .wrap-sheet { display: block; width: 1200px; height: 800px; }
  .serif-caps { font-family: "Cinzel", serif; }
  .serif-num { font-family: "Marcellus", serif; }
  .brand-name { fill: var(--gold); font-family: "Cinzel", serif; font-weight: 600; }
  .on-dark { fill: var(--text-light); }
</style>
</head>
<body>
<svg class="wrap-sheet" viewBox="0 0 1200 800" xmlns="http://www.w3.org/2000/svg" aria-label="Van wrap layout: driver side and rear doors">
  <defs>
    <linearGradient id="goldSweep" x1="0" y1="0" x2="1" y2="0">
      <stop offset="0" stop-color="var(--gold)"/>
      <stop offset="0.55" stop-color="var(--gold-deep)"/>
      <stop offset="1" stop-color="var(--olive)"/>
    </linearGradient>
    <linearGradient id="rearGold" x1="0" y1="0" x2="0" y2="1">
      <stop offset="0" stop-color="var(--olive)"/>
      <stop offset="0.6" stop-color="var(--gold-deep)"/>
      <stop offset="1" stop-color="var(--olive)"/>
    </linearGradient>
    <clipPath id="sideBody">
      <path d="M70 600 L70 482 Q76 444 132 434 L212 422 L292 292 Q302 276 332 274 L788 252 Q812 252 812 274 L812 600 Z"/>
    </clipPath>
    <clipPath id="rearBody">
      <rect x="880" y="250" width="280" height="390" rx="26"/>
    </clipPath>
  </defs>

  <!-- ===== Side elevation ===== -->
  <g class="van-side">
    <g clip-path="url(#sideBody)">
      <rect class="side-base" x="60" y="240" width="760" height="370" fill="var(--wrap-white)"/>
      <path class="side-sweep" d="M60 450 L390 448 Q700 440 790 250 L820 250 L820 610 L60 610 Z" fill="url(#goldSweep)"/>
      <rect class="side-stripe" x="60" y="500" width="760" height="8" fill="var(--black)"/>
      <path class="side-lower-band" d="M60 508 L590 508 Q560 560 540 610 L60 610 Z" fill="var(--burgundy)"/>
      <line x1="212" y1="300" x2="212" y2="600" stroke="#00000033" stroke-width="1.5"/>
      <line x1="372" y1="280" x2="372" y2="600" stroke="#00000033" stroke-width="1.5"/>
      <line x1="590" y1="262" x2="590" y2="440" stroke="#00000022" stroke-width="1.5"/>
    </g>
    <path class="side-window" d="M232 405 L300 300 Q306 292 320 291 L356 291 L356 405 Z" fill="var(--glass)"/>
    <rect class="mirror" x="212" y="370" width="20" height="36" rx="5" fill="var(--black)"/>

    <circle class="brand-mark" cx="396" cy="357" r="12" fill="var(--gold)"/>
    <text class="brand-name" x="416" y="367" font-size="27">BIRCH KEYSTONE</text>
    <text class="brand-name" x="418" y="394" font-size="14" letter-spacing="1">PROPERTY MAINTENANCE</text>

    <text class="serif-caps on-dark" x="224" y="478" font-size="10.5">SHARED LOBBY RESIDENCE</text>
    <text class="serif-caps on-dark" x="224" y="492" font-size="10.5">UPKEEP UNDER S.L.R.U</text>
    <text class="serif-caps on-dark" x="380" y="488" font-size="19">Shared Lobby Residence Upkeep</text>

    <text class="serif-num on-dark" x="300" y="538" font-size="22">WWW.BIRCHKSN.COM</text>
    <text class="serif-num on-dark" x="270" y="588" font-size="40">(555) 314 - 7260</text>

    <g class="service-badge">
      <circle cx="740" cy="532" r="40" fill="var(--burgundy)"/>
      <text class="serif-caps on-dark" x="740" y="522" font-size="10" text-anchor="middle">Servicing</text>
      <text class="serif-caps on-dark" x="740" y="536" font-size="10" text-anchor="middle">Hoboken &amp;</text>
      <text class="serif-caps on-dark" x="740" y="550" font-size="10" text-anchor="middle">Jersey City</text>
    </g>

    <rect class="front-bumper" x="58" y="560" width="30" height="42" rx="4" fill="var(--black)"/>
    <g class="wheel">
      <circle cx="200" cy="600" r="60" fill="var(--page)"/>
      <circle cx="200" cy="604" r="52" fill="var(--tyre)"/>
      <circle cx="200" cy="604" r="28" fill="var(--rim)"/>
    </g>
    <g class="wheel">
      <circle cx="660" cy="600" r="60" fill="var(--page)"/>
      <circle cx="660" cy="604" r="52" fill="var(--tyre)"/>
      <circle cx="660" cy="604" r="28" fill="var(--rim)"/>
    </g>
  </g>

  <!-- ===== Rear elevation ===== -->
  <g class="van-rear">
    <g clip-path="url(#rearBody)">
      <rect x="870" y="240" width="300" height="410" fill="url(#rearGold)"/>
      <path class="rear-window-panel" d="M892 262 L1148 262 L1148 420 Q1020 490 892 420 Z" fill="var(--wrap-white)"/>
      <rect class="rear-band" x="870" y="520" width="300" height="36" fill="var(--black)"/>
      <line x1="1020" y1="262" x2="1020" y2="596" stroke="#00000055" stroke-width="2"/>
      <rect class="rear-footer" x="890" y="600" width="260" height="24" fill="var(--burgundy)"/>
    </g>
    <rect class="tail-light" x="872" y="330" width="14" height="70" rx="3" fill="var(--tail)"/>
    <rect class="tail-light" x="1154" y="330" width="14" height="70" rx="3" fill="var(--tail)"/>

    <circle class="brand-mark" cx="1118" cy="345" r="10" fill="var(--gold)"/>
    <text class="brand-name" x="912" y="348" font-size="19">BIRCH KEYSTONE</text>
    <text class="brand-name" x="914" y="366" font-size="9.5" letter-spacing="0.5">PROPERTY MAINTENANCE</text>

    <text class="serif-caps on-dark" x="1020" y="478" font-size="10.5" text-anchor="middle">SHARED LOBBY RESIDENCE UPKEEP</text>
    <text class="serif-caps on-dark" x="1020" y="493" font-size="10.5" text-anchor="middle">UNDER S.L.R.U</text>
    <text class="serif-num on-dark" x="940" y="544" font-size="13">WWW.BIRCHKSN.COM</text>
    <rect class="plate" x="1080" y="495" width="64" height="30" rx="4" fill="var(--black)"/>
    <rect x="1086" y="500" width="52" height="20" rx="2" fill="#3a6fb0"/>
    <text class="serif-num on-dark" x="1146" y="588" font-size="28" text-anchor="end">(555) 314 - 7260</text>
    <text class="serif-caps on-dark" x="1020" y="616" font-size="10.5" text-anchor="middle">Servicing Hoboken &amp; Jersey City</text>

    <rect class="rear-bumper" x="872" y="640" width="296" height="30" rx="6" fill="var(--black)"/>
    <rect class="rear-tyre" x="900" y="670" width="46" height="40" rx="6" fill="var(--tyre)"/>
    <rect class="rear-tyre" x="1094" y="670" width="46" height="40" rx="6" fill="var(--tyre)"/>
  </g>
</svg>
</body>
</html>
```